Business Card Design for Flood Rescue 360 - Property Restoration Professionals

I need a business card designed for Flood Rescue 360. We are a full-service property restoration solution. Providing water, fire, smoke & storm restoration as well as mold remediation and full remodel or reconstruction to homes and businesses across Dallas-Fort Worth, TX.
Target Market(s)
home and business owners with insurance covered property damage from water, fire or storm related damage
Industry/Entity Type
property restoration
Contact Information for Business Card
Martin Kell General Manager Cell: 214-555-0193 Office: 469-555-0148 email: Martin@FloodRescue360.example services: Water, Fire, Mold, Reconstruction Tagline: Fast Help When Water Strikes!
Look and feel
Each slider illustrates characteristics of the customer's brand and the style your logo design should communicate.

```html
<!DOCTYPE html>
<html lang="en">
<head>
<meta charset="utf-8">
<title>Flood Rescue 360 – Business Card</title>
<link href="https://fonts.googleapis.com/css2?family=Montserrat:wght@400;500;800&family=Arimo:wght@400;700&display=swap" rel="stylesheet">
<style>
  :root {
    --bg: #d5d8d9;
    --paper: #f7f7f6;
    --blue: #1b9ad6;
    --ink: #3c3e41;
    --grey: #55585c;
  }
  * { box-sizing: border-box; margin: 0; padding: 0; }
  html, body { width: 1200px; height: 829px; overflow: hidden; background: var(--bg); }
  .stage { position: relative; width: 1200px; height: 829px; }
  .card {
    position: absolute; top: 266px; width: 520px; height: 297px;
    background: var(--paper); overflow: hidden;
    box-shadow: 0 10px 24px rgba(0,0,0,.18);
    border-bottom: 4px solid var(--blue);
  }
  .card--front { left: 50px; }
  .card--back { left: 630px; }

  /* front */
  .contact { position: absolute; left: 34px; top: 40px; font-family: "Arimo", sans-serif; }
  .contact__name { color: var(--blue); font-weight: 700; font-size: 24px; letter-spacing: .5px; text-transform: uppercase; }
  .contact__title { color: var(--grey); font-size: 15px; margin-top: 2px; }
  .contact__list { list-style: none; margin-top: 20px; }
  .contact__item { display: flex; align-items: center; gap: 8px; color: var(--ink); font-size: 14.5px; line-height: 22px; }
  .contact__icon { width: 11px; height: 11px; flex: none; }
  .brand-name {
    position: absolute; right: 34px; bottom: 30px;
    font-family: "Montserrat", sans-serif; font-weight: 800; font-size: 24px; line-height: 1;
    color: var(--blue); text-transform: uppercase; white-space: nowrap;
  }

  /* back */
  .wordmark {
    position: absolute; left: 0; right: 0; top: 60px; text-align: center;
    font-family: "Montserrat", sans-serif; font-weight: 800; font-size: 44px; line-height: 1;
    color: var(--blue); text-transform: uppercase; letter-spacing: -.5px;
  }
  .services {
    position: absolute; left: 0; right: 0; top: 150px; text-align: center;
    font-family: "Montserrat", sans-serif; font-weight: 500; font-size: 15px; letter-spacing: 1px; color: var(--ink);
  }
  .services__sep { color: var(--blue); margin: 0 6px; }
  .band {
    position: absolute; left: 0; right: 0; top: 182px; height: 30px; background: var(--blue);
    display: flex; align-items: center; justify-content: center;
    font-family: "Montserrat", sans-serif; font-weight: 500; font-size: 14px; letter-spacing: 1px; color: #fff;
  }
</style>
</head>
<body>
<main class="stage">
  <section class="card card--front" aria-label="Business card front">
    <div class="contact">
      <h1 class="contact__name">Martin Kell</h1>
      <p class="contact__title">General Manager</p>
      <ul class="contact__list">
        <li class="contact__item">
          <svg class="contact__icon" viewBox="0 0 12 12"><path d="M1 4c0-2 2-3 5-3s5 1 5 3l-3 1-1-1H5L4 5zM2 6h8v5H2z" fill="var(--blue)"/></svg>
          469-555-0148</li>
        <li class="contact__item">
          <svg class="contact__icon" viewBox="0 0 12 12"><rect x="3" y="0.5" width="6" height="11" rx="1.2" fill="none" stroke="var(--blue)" stroke-width="1.3"/></svg>
          214-555-0193</li>
        <li class="contact__item">
          <svg class="contact__icon" viewBox="0 0 12 12"><rect x="0.5" y="2.5" width="11" height="7" fill="var(--blue)"/><path d="M0.5 2.5L6 7l5.5-4.5" fill="none" stroke="#fff" stroke-width="1"/></svg>
          Martin@FloodRescue360.example</li>
        <li class="contact__item">
          <svg class="contact__icon" viewBox="0 0 12 12"><circle cx="6" cy="6" r="5.5" fill="var(--blue)"/><path d="M0.5 6h11M6 .5c-3 3-3 8 0 11M6 .5c3 3 3 8 0 11" fill="none" stroke="#fff" stroke-width=".8"/></svg>
          www.FloodRescue360.example</li>
      </ul>
    </div>
    <p class="brand-name">Flood Rescue 360</p>
  </section>

  <section class="card card--back" aria-label="Business card back">
    <h2 class="wordmark">Flood Rescue 360</h2>
    <p class="services">Water<span class="services__sep">•</span>Fire<span class="services__sep">•</span>Mold<span class="services__sep">•</span>Reconstruction</p>
    <p class="band">Fast Help When Water Strikes!</p>
  </section>
</main>
</body>
</html>
```